Real estate broker business card

Want a modern celan but effective business card for my residential and commercial real estate business. I want the back of the card to advertise my services and to capture business. I have attached the back of my current business card fore ideas

Target Market(s)

home buyers and seller. commercial buyers and sellers

Industry/Entity Type

Real Estate

Contact Information for Business Card

must have my contact information and my photo

Requirements
Must have
• Corla Vintreff
• Owner & Qualifying Broker
• Vintreff Real Estate Services
• 505.718.2947
• corla@vintreffhomes.com
• www.vintreffhomes.com
Nice to have
• metallic
• Business capture text: " Don't buy or lease property without someone looking out for your best interests. I will represent you on your home or investment purchase for FREE!"
• "Home owners, call today to receive a FREE market analysis for your homes value!

```html
<!DOCTYPE html>
<html lang="en">
<head>
<meta charset="utf-8">
<title>Vintreff Real Estate Services – Business Card</title>
<link href="https://fonts.googleapis.com/css2?family=Cinzel:wght@500&family=Montserrat:wght@400;600&display=swap" rel="stylesheet">
<style>
  :root {
    --backdrop: #e8e9eb;
    --card-black: #050505;
    --teal: #1a8c9b;
    --teal-dark: #0f6470;
    --text-gray: #9a9a9a;
    --contact-gray: #b9b9b9;
    --silver-light: #eeeeee;
    --silver-mid: #b4b4b4;
    --photo-green: #2f4a2c;
    --photo-deep: #15220f;
  }
  html, body {
    margin: 0;
    padding: 0;
    width: 1200px;
    height: 1000px;
    overflow: hidden;
    background: var(--backdrop);
  }
  .canvas { position: relative; width: 1200px; height: 1000px; }
  .card {
    position: absolute;
    left: 279px;
    width: 643px;
    height: 376px;
    background: var(--card-black);
    box-shadow: 3px 5px 6px rgba(0,0,0,0.35);
    overflow: hidden;
  }
  .card--front { top: 120px; }
  .card--back { top: 539px; }

  .metal-band {
    position: absolute;
    left: 0;
    right: 0;
    background: linear-gradient(100deg, var(--silver-mid), var(--silver-light) 50%, var(--silver-mid));
  }
  .teal-rule {
    position: absolute;
    left: 0;
    right: 0;
    height: 8px;
    background: var(--teal-dark);
  }
  .card--front .metal-band--top { top: 0; height: 62px; }
  .card--front .teal-rule--top { top: 62px; }
  .card--front .teal-rule--bottom { top: 312px; }
  .card--front .metal-band--bottom { top: 320px; height: 56px; }
  .card--back .teal-rule--bottom { top: 326px; z-index: 2; }
  .card--back .metal-band--bottom { top: 334px; height: 42px; z-index: 2; }

  .brand-front {
    position: absolute;
    left: 0;
    right: 0;
    top: 96px;
    text-align: center;
    font-family: "Cinzel", serif;
    font-weight: 500;
  }
  .brand-front .brand-dot {
    display: block;
    width: 86px;
    height: 86px;
    margin: 0 auto 14px;
    border-radius: 50%;
    background: var(--teal);
  }
  .brand-front .brand-name {
    display: block;
    font-size: 46px;
    line-height: 1;
    color: var(--teal);
  }
  .brand-front .brand-tag {
    display: block;
    font-family: "Montserrat", sans-serif;
    font-size: 15px;
    letter-spacing: 2.4px;
    margin-top: 4px;
    color: var(--text-gray);
  }
  .brand-back {
    position: absolute;
    left: 34px;
    top: 34px;
    display: flex;
    align-items: center;
    gap: 10px;
    font-family: "Cinzel", serif;
    font-weight: 500;
  }
  .brand-back .brand-dot {
    width: 72px;
    height: 72px;
    border-radius: 50%;
    background: var(--teal);
  }
  .brand-back .brand-name {
    display: block;
    font-size: 40px;
    line-height: 1;
    color: var(--teal);
  }
  .brand-back .brand-tag {
    display: block;
    font-family: "Montserrat", sans-serif;
    font-weight: 600;
    font-size: 12.5px;
    letter-spacing: 1.6px;
    margin-top: 4px;
    color: var(--text-gray);
  }
  .agent { position: absolute; left: 61px; top: 166px; }
  .agent-name {
    margin: 0;
    font-family: "Cinzel", serif;
    font-weight: 500;
    font-size: 30px;
    color: var(--teal);
    line-height: 1.1;
  }
  .agent-title {
    margin: 2px 0 0;
    font-family: "Montserrat", sans-serif;
    font-size: 18px;
    color: var(--text-gray);
  }
  .contact-list {
    position: absolute;
    left: 61px;
    top: 245px;
    margin: 0;
    padding: 0;
    list-style: none;
    font-family: "Montserrat", sans-serif;
    font-size: 15px;
    color: var(--contact-gray);
  }
  .contact-list li { display: flex; align-items: center; gap: 6px; height: 21px; }
  .contact-icon { width: 17px; height: 17px; flex: none; }
  .agent-photo {
    position: absolute;
    left: 394px;
    top: 56px;
    width: 223px;
    height: 275px;
    background: radial-gradient(ellipse at 50% 45%, #4a5a40 0%, var(--photo-green) 55%, var(--photo-deep) 100%);
  }
</style>
</head>
<body>
<main class="canvas">

  <section class="card card--front" aria-label="Card front">
    <div class="metal-band metal-band--top" role="img" aria-label="Brushed silver metallic finish"></div>
    <div class="teal-rule teal-rule--top"></div>
    <div class="brand-front">
      <span class="brand-dot"></span>
      <span class="brand-name">VINTREFF</span>
      <span class="brand-tag">REAL ESTATE SERVICES</span>
    </div>
    <div class="teal-rule teal-rule--bottom"></div>
    <div class="metal-band metal-band--bottom" role="img" aria-label="Brushed silver metallic finish"></div>
  </section>

  <section class="card card--back" aria-label="Card back">
    <div class="brand-back">
      <span class="brand-dot"></span>
      <div>
        <span class="brand-name">VINTREFF</span>
        <span class="brand-tag">REAL ESTATE SERVICES</span>
      </div>
    </div>

    <div class="agent">
      <h1 class="agent-name">Corla Vintreff</h1>
      <p class="agent-title">Owner &amp; Qualifying Broker</p>
    </div>

    <ul class="contact-list">
      <li>
        <svg class="contact-icon" viewBox="0 0 16 16" aria-hidden="true"><circle cx="8" cy="8" r="8" fill="var(--teal)"/><path d="M5 11.5 L10.5 4.5 L11.8 5.6 L6.3 12.5 Z" fill="var(--card-black)"/></svg>
        505.718.2947
      </li>
      <li>
        <svg class="contact-icon" viewBox="0 0 16 16" aria-hidden="true"><circle cx="8" cy="8" r="8" fill="var(--teal)"/><rect x="4" y="5" width="8" height="6" fill="var(--card-black)"/><path d="M4 5 L8 8.5 L12 5" stroke="var(--teal)" stroke-width="1" fill="none"/></svg>
        corla@vintreffhomes.com
      </li>
      <li>
        <svg class="contact-icon" viewBox="0 0 16 16" aria-hidden="true"><circle cx="8" cy="8" r="8" fill="var(--teal)"/><circle cx="8" cy="8" r="4.2" fill="none" stroke="var(--card-black)" stroke-width="1.3"/><path d="M3.8 8 H12.2 M8 3.8 V12.2" stroke="var(--card-black)" stroke-width="1"/></svg>
        www.vintreffhomes.com
      </li>
    </ul>

    <div class="agent-photo" role="img" aria-label="Portrait photo of the broker against a leafy green background"></div>

    <div class="teal-rule teal-rule--bottom"></div>
    <div class="metal-band metal-band--bottom" role="img" aria-label="Brushed silver metallic finish"></div>
  </section>

</main>
</body>
</html>
```